Website for boutique digital agency helping high-tech startups accelerate growth.

We need a website design for a relatively young company based in Mauritius called 'LoomTrax'.

We are a professional services firm delivering digital infrastructure for revenue operations (RevOps)*.

Entrepreneurial startups and SMBs in the technology sector work with us to accelerate growth by delivering extraordinary customer experiences across the full customer lifecycle.

We would like a colourful design that utilises the (4) colours of our existing logo design.

The final design should communicate dynamic growth through relentless customer focus.
----------------------------------------------------------
*Revenue Operations (RevOps) is the strategic alignment of sales, marketing and customer success operations to accelerate growth by delivering extraordinary customer experiences across the full customer life cycle.
Updates

Target Market(s)

Entrepreneurial startups and SMBs (Small/Medium Businesses) in the technology sector.

Question: Why the technology sector?

Answer: Because technology entrepreneurs often have a tremendous challenge to effectively communicate to the market and to prospective customers the value and the benefits of their products & services due to the inherent complexity of technological innovation.

LoomTrax is a team of creatively-minded engineers and technologists who have worked with and understand the technologies and innovations our clients are passionate about bringing to market.

Industry/Entity Type

Professional Service

Number of Pages Required

5+ page

Font styles to use
Sans Serif

Requirements
Must have
• Minimalistic designs rich with visual meaning are highly preferred. Mobile responsive designs are also required. Must show how designs render on Desktop, Tablet and Smartphone devices.

Website pages:
1) Homepage: problem statement, target customers, value proposition & benefits
2) Services: 3-4 tiers of services packages with pricing and "how to work with us"
3) Resources: links to all kinds of relevant materials
4) Contact Us: contact form and special project quote form
5) Blog: matrix design with featured images for each post
Nice to have
• Bold, interesting, colourful, inspiring images that visually communicate:
- relentless customer focus
- extraordinary, memorable experiences
- business at the speed of innovation
Should not have
• Any meme or theme that panders to "political correctness".

```html
<!DOCTYPE html>
<html lang="en">
<head>
<meta charset="utf-8">
<title>LoomTrax — Home</title>
<link rel="stylesheet" href="https://fonts.googleapis.com/css2?family=Arimo:wght@400;700&family=Raleway:wght@200;300;400;500&display=swap">
<style>
  :root {
    --page: #ffffff;
    --ink: #333333;
    --ink-soft: #555555;
    --ink-muted: #6a6a6a;
    --teal: #1a7f7a;
    --orange: #f26522;
    --red: #e8173f;
    --green: #7ac143;
    --navy: #0f2a3a;
    --rule: #c8c8c8;
    --scene-top: #eef4fa;
    --scene-bottom: #dbe8f4;
    --mist: #e6f1f8;
  }
  * { box-sizing: border-box; margin: 0; padding: 0; }
  html, body { width: 1200px; height: 800px; overflow: hidden; background: var(--page); }
  body { position: relative; font-family: "Raleway", sans-serif; color: var(--ink); }

  .brand {
    position: absolute; left: 52px; top: 86px;
    display: flex; align-items: center; gap: 8px;
    font-family: "Arimo", sans-serif; font-weight: 700; font-size: 22px;
    color: var(--ink-soft); letter-spacing: 0.2px;
  }
  .brand-mark { width: 14px; height: 14px; background: var(--teal); }

  .main-nav { position: absolute; top: 36px; right: 57px; display: flex; gap: 27px; }
  .main-nav a {
    font-family: "Arimo", sans-serif; font-size: 13px; text-decoration: none;
    color: var(--teal); letter-spacing: 0.2px;
  }
  .main-nav a.is-current { color: var(--orange); }

  .social-rail {
    position: absolute; left: 0; top: 297px; width: 49px; height: 265px;
    background: var(--navy);
    display: flex; flex-direction: column; align-items: center; justify-content: center; gap: 38px;
  }
  .social-rail .social-dot { width: 18px; height: 18px; border-radius: 50%; background: #ffffff; display: block; }

  .hero-quote {
    position: absolute; left: 99px; top: 214px;
    font-family: "Arimo", sans-serif; font-weight: 400;
    font-size: 48px; line-height: 58px; color: var(--ink-soft);
  }
  .quote-open, .quote-close {
    position: absolute; font-family: "Arimo", sans-serif; font-weight: 700; font-size: 30px; line-height: 1;
  }
  .quote-open { left: 72px; top: 203px; color: var(--red); }
  .quote-close { left: 545px; top: 330px; color: var(--teal); }

  .hero-illustration {
    position: absolute; left: 705px; top: 170px; width: 366px; height: 283px;
    background: linear-gradient(180deg, var(--scene-top) 0%, var(--scene-bottom) 100%);
  }

  .hex-field {
    position: absolute; right: 0; bottom: 0; width: 255px; height: 330px;
    background: linear-gradient(160deg, rgba(230,241,248,0) 0%, var(--mist) 100%);
  }

  .revenue-heading {
    position: absolute; left: 100px; top: 447px;
    font-size: 19px; font-weight: 400; color: var(--red); letter-spacing: 0.1px;
  }
  .intro-copy {
    position: absolute; left: 99px; top: 484px;
    font-size: 17px; line-height: 26.6px; font-weight: 400; color: var(--ink);
    white-space: nowrap;
  }
  .intro-copy .name { color: var(--ink-muted); }

  .divider {
    position: absolute; left: 503px; top: 497px; width: 2px; height: 149px; background: var(--rule);
  }
  .divider::after {
    content: ""; position: absolute; left: 0; top: 44px; width: 2px; height: 10px; background: var(--red);
  }

  .practices-title {
    position: absolute; left: 534px; top: 496px;
    font-size: 34px; line-height: 40px; font-weight: 300; color: var(--green); letter-spacing: 0.5px;
  }

  .practice { position: absolute; display: flex; align-items: baseline; white-space: nowrap; }
  .practice-num { font-size: 60px; font-weight: 200; color: var(--orange); line-height: 1; margin-right: 2px; }
  .practice-text { font-size: 22px; font-weight: 400; color: var(--teal); line-height: 1; }
  .practice-1 { left: 807px; top: 522px; }
  .practice-1 .practice-num { margin-right: 10px; }
  .practice-2 { left: 749px; top: 567px; }
  .practice-3 { left: 684px; top: 617px; }
  .practice-4 { left: 630px; top: 661px; }
  .practice-4 .practice-num { margin-right: 6px; }

  .site-footer {
    position: absolute; left: 52px; right: 57px; top: 758px;
    display: flex; justify-content: space-between;
    font-family: "Arimo", sans-serif; font-size: 11px; color: var(--ink);
  }
  .site-footer .legal-links { color: var(--ink-muted); }
</style>
</head>
<body>
  <header>
    <div class="brand"><span class="brand-mark"></span>loomtrax.io</div>
    <nav class="main-nav">
      <a class="is-current" href="#">HOME</a>
      <a href="#">SERVICES</a>
      <a href="#">RESOURCES</a>
      <a href="#">CONTACT US</a>
    </nav>
  </header>

  <aside class="social-rail" aria-label="Social links">
    <span class="social-dot" aria-label="Social network 1"></span>
    <span class="social-dot" aria-label="Social network 2"></span>
    <span class="social-dot" aria-label="Social network 3"></span>
    <span class="social-dot" aria-label="Social network 4"></span>
  </aside>

  <main>
    <span class="quote-open">“</span>
    <h1 class="hero-quote">When the world is<br>changing, it’s time to<br>change your world</h1>
    <span class="quote-close">”</span>

    <div class="hero-illustration" role="img" aria-label="Illustration of a business team launching a rocket from a computer screen toward growth"></div>
    <div class="hex-field" role="img" aria-label="Faint hexagon network pattern"></div>

    <h2 class="revenue-heading">MAXIMIZE YOUR REVENUE STREAM</h2>
    <p class="intro-copy"><span class="name">LoomTrax</span> is a team of creatively-minded<br>engineers and technologists who have<br>worked with and understand the<br>technologies and innovations our clients are<br>passionate about bringing to market . We<br>are a professional services firm .</p>

    <div class="divider"></div>

    <h2 class="practices-title">LOOMTRAX<br>BEST<br>PRACTICES</h2>
    <div class="practice practice-1"><span class="practice-num">1</span><span class="practice-text">QUESTION THE STATUS QUO.</span></div>
    <div class="practice practice-2"><span class="practice-num">2</span><span class="practice-text">AUTOMATION IS A MUST.</span></div>
    <div class="practice practice-3"><span class="practice-num">3</span><span class="practice-text">FOCUS ON THE END USER.</span></div>
    <div class="practice practice-4"><span class="practice-num">4</span><span class="practice-text">THINK SCALABILITY &nbsp;AND GROWTH.</span></div>
  </main>

  <footer class="site-footer">
    <span>© 2020 LoomTrax.io™ All Rights Reserved</span>
    <span class="legal-links">. Privacy Policy | Sitemap</span>
  </footer>
</body>
</html>
```